Business Stationary & Card Design

Double sided business cards, letterhead, horizontal brochure, and envelope design using our logo. We want a modern minimal look. One side of the business card should be only our logo and maybe our slogan "Get It Done Right". The other side should include our coil spring and not the logo again. Watermark like (or not) positioned partially, horizontal, on angle, or a combination of. IF a background color or accent color is used we like blue (4885ed). The letterhead, brochure, and envelope design should be similar to the card. Except no solid background color.Maybe the spring at the bottom of the letterhead page watermark style and partial. Additional info on the business card should be present:
Employee Name
Position
Phone
Email
Address
The final design should communicate strength, simplicity, and newness.

Target Market(s)

35-55 Male & Female

Industry/Entity Type

Automotive

Contact Information for Business Card

One side of the double sided business card should be only our logo and maybe our slogan "Get It Done Right". The other side should include our coil spring and not the logo again. Watermark like (or not) positioned partially, horizontal, on angle, or a combination of. IF a background color or accent color is used we like blue (4885ed). Additional info on the business card should be present:
Employee Name
Position
Phone
Email
Address

Font styles to use
Other font styles liked:
• Use font that compliments the attached font. Maybe plain eurostyle?

Colors
0492cd
3276b5

Requirements
Must have
• Use the coil spring in a subtle unique way (s). Double sided business card
Should not have
• Clutter, colors that do not coordinate well with our logo. Fonts that do not compliment our font.

```html
<!DOCTYPE html>
<html lang="en">
<head>
<meta charset="utf-8">
<title>Ketter Auto — Stationery</title>
<link href="https://fonts.googleapis.com/css2?family=Michroma&family=Roboto:wght@400;500&display=swap" rel="stylesheet">
<style>
  :root {
    --canvas: #dedede;
    --paper: #f4f4f4;
    --paper-light: #f7f7f7;
    --brand-yellow: #e3bd1b;
    --brand-blue: #4885ed;
    --ink: #3a3a3a;
    --ink-dark: #1e1e1e;
    --watermark: #e4e4e4;
    --watermark-edge: #ececec;
  }
  * { box-sizing: border-box; margin: 0; padding: 0; }
  html, body { width: 1200px; height: 1025px; overflow: hidden; }
  body {
    position: relative;
    background: var(--canvas);
    font-family: "Roboto", Arial, sans-serif;
    color: var(--ink);
  }
  .sheet { position: absolute; overflow: hidden; }

  .wordmark {
    font-family: "Michroma", "Eurostile", sans-serif;
    font-weight: 400;
    color: var(--brand-yellow);
    letter-spacing: 1px;
    white-space: nowrap;
    display: block;
  }

  .coil-watermark {
    position: absolute;
    background: linear-gradient(90deg, var(--watermark-edge) 0%, var(--watermark) 60%, var(--watermark) 100%);
    border-radius: 40px 0 0 40px;
  }

  /* Letterhead */
  .letterhead { left: 80px; top: 75px; width: 617px; height: 868px; background: var(--paper); }
  .letterhead .wordmark { position: absolute; top: 72px; left: 0; width: 100%; text-align: center; font-size: 26px; }
  .letterhead .coil-watermark { left: 378px; top: 304px; width: 239px; height: 564px; }
  .letterhead-footer {
    position: absolute; top: 799px; left: 0; width: 100%;
    text-align: center; font-size: 9.5px; color: var(--ink);
  }
  .letterhead-band {
    position: absolute; top: 824px; left: 0; width: 100%; height: 21px;
    background: var(--brand-blue); color: #fff;
    font-size: 9px; letter-spacing: 2px; text-align: center; line-height: 21px;
  }

  /* Business card — contact side */
  .card-contact { left: 784px; top: 101px; width: 331px; height: 190px; background: var(--paper-light); }
  .card-contact .coil-watermark { left: 243px; top: 0; width: 88px; height: 190px; border-radius: 30px 0 0 30px; }
  .card-name { position: absolute; left: 31px; top: 27px; font-size: 12px; color: var(--brand-yellow); font-weight: 500; }
  .card-role { position: absolute; left: 31px; top: 44px; font-size: 8px; color: var(--ink-dark); letter-spacing: .4px; }
  .card-address { position: absolute; left: 31px; top: 98px; font-size: 8px; line-height: 11px; }
  .card-lines { position: absolute; left: 31px; top: 128px; list-style: none; font-size: 8px; line-height: 10.5px; }
  .card-lines li { display: flex; align-items: center; gap: 5px; }
  .card-lines svg { width: 7px; height: 7px; fill: var(--brand-yellow); }

  /* Business card — logo side */
  .card-brand { left: 783px; top: 326px; width: 332px; height: 189px; background: var(--brand-blue); }
  .card-brand .wordmark { position: absolute; top: 72px; width: 100%; text-align: center; font-size: 24px; }
  .card-slogan {
    position: absolute; top: 148px; width: 100%; text-align: center;
    font-family: "Michroma", sans-serif; font-size: 10.5px; color: #fff; letter-spacing: .5px;
  }

  /* Envelope */
  .envelope { left: 493px; top: 564px; width: 622px; height: 283px; background: var(--paper-light); }
  .envelope .coil-watermark { left: 493px; top: 0; width: 129px; height: 283px; }
  .envelope .wordmark { position: absolute; left: 45px; top: 42px; font-size: 15px; }
  .envelope-address { position: absolute; left: 45px; top: 80px; width: 143px; text-align: center; font-size: 9.5px; line-height: 12px; }
</style>
</head>
<body>

  <section class="sheet letterhead">
    <span class="wordmark">KETTER AUTO</span>
    <div class="coil-watermark" role="img" aria-label="Faint partial coil spring watermark"></div>
    <p class="letterhead-footer">2140 Larkspur Avenue, Fairbanks, Alaska 34820 | 512 308 7741 | dana@ketterauto.com</p>
    <div class="letterhead-band">www.ketterauto.com</div>
  </section>

  <section class="sheet card-contact">
    <div class="coil-watermark" role="img" aria-label="Faint partial coil spring watermark"></div>
    <p class="card-name">DANA WHITFIELD</p>
    <p class="card-role">CEO/FOUNDER</p>
    <p class="card-address">2140 Larkspur Avenue<br>Fairbanks, Alaska 34820</p>
    <ul class="card-lines">
      <li><svg viewBox="0 0 10 10"><path d="M2 0.5 L4 2.6 L3 3.8 Q4.2 6 6.2 7 L7.4 6 L9.5 8 L8 9.6 Q4 9 0.5 2 Z"/></svg>512 308 7741</li>
      <li><svg viewBox="0 0 10 10"><path d="M0.5 2 H9.5 V8.5 H0.5 Z M0.5 2 L5 5.5 L9.5 2" /></svg>dana@ketterauto.com</li>
      <li><svg viewBox="0 0 10 10"><circle cx="5" cy="5" r="4.5"/></svg>www.ketterauto.com</li>
    </ul>
  </section>

  <section class="sheet card-brand">
    <span class="wordmark">KETTER AUTO</span>
    <p class="card-slogan">Get It Done Right</p>
  </section>

  <section class="sheet envelope">
    <div class="coil-watermark" role="img" aria-label="Faint partial coil spring watermark"></div>
    <span class="wordmark">KETTER AUTO</span>
    <p class="envelope-address">2140 Larkspur Avenue<br>Fairbanks, Alaska 34820</p>
  </section>

</body>
</html>
```